Business Card Design Project

New Business Card design for Varodine Technology Ltd using new Logo and new Tagline for staffing company.

About us from our website - www.varodine.example:

VaroDine is a leading and recognized Electronic Entertainment, Workforce Augmentation, and Project Management solutions provider with clients in Electronic Entertainment, Legal, Technology, Government and other verticals that range in size from start up organizations to Zenlar 500 companies. VaroDine is certified as an 8(a) minority and woman owned enterprise, established in 1998.

Target Market(s)

Companies in Electronic Entertainment, Legal, Government and Technology

Industry/Entity Type

Business

Requirements
Must have
• Must include in small letters the following information on back:

Established in 1998
8(a)(w)(e), Cage #7KRT9, DUNS #462137580

Front should have the following:
Derek Holloway
Vice President
5820 Birchmont Road
Fallowby, FB 482917
555-318-2746 X 100
555-902-6613 Fax
555-318-2746 Toll Free
name@varodine.example

Our Tagline: Connect • Collaborate • Achieve

```html
<!DOCTYPE html>
<html lang="en">
<head>
<meta charset="utf-8">
<title>VaroDine Business Card</title>
<link rel="stylesheet" href="https://fonts.googleapis.com/css2?family=Arimo:wght@400;700&display=swap">
<style>
  :root {
    --brand-blue: #0b5cad;
    --brand-blue-text: #1766bf;
    --card-black: #000000;
    --ink-white: #ffffff;
    --page-bg: #ffffff;
    --card-radius: 18px;
  }
  * { box-sizing: border-box; margin: 0; padding: 0; }
  html, body {
    width: 1200px;
    height: 900px;
    overflow: hidden;
    background: var(--page-bg);
    font-family: "Arimo", Arial, sans-serif;
  }
  .canvas { position: relative; width: 1200px; height: 900px; }

  .card {
    position: absolute;
    width: 670px;
    height: 395px;
    border-radius: var(--card-radius);
    overflow: hidden;
  }

  /* Front */
  .card-front { left: 40px; top: 60px; background: var(--card-black); }
  .card-front .wordmark {
    position: absolute;
    left: 0; top: 120px;
    width: 320px;
    text-align: center;
    color: var(--ink-white);
    font-weight: 700;
    font-size: 54px;
    letter-spacing: -1px;
  }
  .card-front .divider {
    position: absolute;
    left: 318px; top: 20px;
    width: 3px; height: 230px;
    background: linear-gradient(to bottom, rgba(11,92,173,0) 0%, var(--brand-blue) 30%, var(--brand-blue) 65%, rgba(11,92,173,0) 100%);
    box-shadow: -6px 0 14px rgba(11,92,173,0.45);
  }
  .card-front .contact-block {
    position: absolute;
    left: 372px; top: 30px;
  }
  .person-name {
    color: var(--brand-blue-text);
    font-weight: 700;
    font-size: 29px;
    line-height: 1.05;
  }
  .person-title {
    color: var(--ink-white);
    font-weight: 700;
    font-size: 23px;
    line-height: 1.15;
    margin-bottom: 22px;
  }
  .contact-lines {
    list-style: none;
    color: var(--brand-blue-text);
    font-size: 14.5px;
    line-height: 1.3;
  }
  .tagline-band {
    position: absolute;
    left: 0; bottom: 0;
    width: 100%; height: 72px;
    background: var(--brand-blue);
    display: flex;
    justify-content: space-around;
    align-items: center;
    padding: 0 40px;
  }
  .tagline-band span {
    color: var(--card-black);
    font-weight: 700;
    font-size: 23px;
  }

  /* Back */
  .card-back {
    left: 490px; top: 470px;
    background: var(--brand-blue);
    color: var(--ink-white);
    text-align: center;
    font-weight: 700;
  }
  .card-back .established {
    position: absolute;
    top: 0; left: 0; width: 100%; height: 86px;
    display: flex; align-items: center; justify-content: center;
    font-size: 17px;
  }
  .card-back .logo-band {
    position: absolute;
    top: 86px; left: 0;
    width: 100%; height: 205px;
    background: var(--card-black);
    display: flex; align-items: center; justify-content: center;
  }
  .card-back .wordmark {
    color: var(--ink-white);
    font-weight: 700;
    font-size: 66px;
    letter-spacing: -1px;
  }
  .card-back .registrations {
    position: absolute;
    top: 303px; left: 0; width: 100%;
    list-style: none;
    font-size: 16.5px;
    line-height: 1.25;
  }
</style>
</head>
<body>
<main class="canvas">
  <section class="card card-front" aria-label="Business card front">
    <div class="wordmark">VaroDine</div>
    <div class="divider"></div>
    <div class="contact-block">
      <h1 class="person-name">Derek Holloway</h1>
      <p class="person-title">Vice President</p>
      <ul class="contact-lines">
        <li>5820 Birchmont Road</li>
        <li>Fallowby, FB 482917</li>
        <li>555-318-2746 X 100</li>
        <li>555-902-6613 Fax</li>
        <li>555-318-2746 Toll Free</li>
        <li>name@varodine.example</li>
      </ul>
    </div>
    <div class="tagline-band">
      <span>Connect</span>
      <span>Collaborate</span>
      <span>Achieve</span>
    </div>
  </section>

  <section class="card card-back" aria-label="Business card back">
    <p class="established">Established in 1998</p>
    <div class="logo-band">
      <div class="wordmark">VaroDine</div>
    </div>
    <ul class="registrations">
      <li>8(a)(w)(e)</li>
      <li>Cage #7KRT9</li>
      <li>DUNS #462137580</li>
    </ul>
  </section>
</main>
</body>
</html>
```